Not-for-profit Community Law Business Card

Not-for-Profit community law firm are looking for new business card design to accompany a new logo.
The cards are to assist the organisation in reaching their strategic objective of generating greater networking amongst the community; specifically with other service providers, clients, and community influencers.
It should stand out. Be professional, strong, creative, clear in detail. The logo should be a major feature of the design.
Updates

Hi All,

Thank you for the submissions so far. I have uploaded the logo and colour details again, as requested. If you have any further issues downloading them or need a different format please contact me on jess_harlow@bvm.net.au

Kind regards,

Industry/Entity Type

Law Firm

Requirements
Must have
• Logo (attached)
Person's name
Position
Phone
Fax
Email
PO Box address
Website
Colours from the logo.

```html
<!DOCTYPE html>
<html lang="en">
<head>
<meta charset="utf-8">
<title>Northgate Law Collective – Business Card</title>
<link rel="stylesheet" href="https://fonts.googleapis.com/css2?family=Arimo:wght@400;700&display=swap">
<style>
  :root {
    --stage: #f1f1f2;
    --card: #ffffff;
    --brand-blue: #1175be;
    --ink: #111111;
    --rule: #b5b5b5;
    --white: #ffffff;
  }
  * { box-sizing: border-box; margin: 0; padding: 0; }
  html, body {
    width: 1200px; height: 900px; overflow: hidden;
    background: var(--stage);
    font-family: "Arimo", Arial, sans-serif;
  }
  .stage { position: relative; width: 1200px; height: 900px; }

  .card-front {
    position: absolute; left: 132px; top: 144px;
    width: 504px; height: 290px;
    background: var(--card);
  }
  .front-brand {
    position: absolute; left: 28px; top: 40px;
    display: flex; align-items: center; gap: 8px;
  }
  .front-brand .brand-dot {
    width: 18px; height: 18px; border-radius: 50%;
    background: var(--brand-blue);
  }
  .front-brand .brand-name {
    color: var(--brand-blue); font-weight: 700;
    font-size: 15px; line-height: 1; white-space: nowrap;
  }

  .holder {
    position: absolute; left: 0; right: 0; top: 98px;
    text-align: center; color: var(--ink); font-weight: 700;
    font-size: 16px; line-height: 1.15;
  }
  .divider {
    position: absolute; left: 58px; right: 56px; top: 144px;
    border-top: 1.5px solid var(--rule);
  }
  .contact-list {
    position: absolute; left: 56px; top: 160px;
    list-style: none; color: var(--ink);
    font-size: 15px; line-height: 21px;
    white-space: nowrap;
  }
  .contact-list .label { display: inline-block; min-width: 22px; }
  .contact-list .label-wide { min-width: 38px; }

  .web-band {
    position: absolute; left: 0; right: 0; bottom: 0; height: 32px;
    background: var(--brand-blue); color: var(--white);
    font-weight: 700; font-size: 15px;
    display: flex; align-items: center; justify-content: center;
  }

  .card-back {
    position: absolute; left: 552px; top: 468px;
    width: 506px; height: 288px;
    background: var(--brand-blue);
    display: flex; align-items: center; justify-content: center;
  }
  .back-brand {
    display: flex; align-items: center; gap: 12px;
  }
  .back-brand .brand-dot {
    width: 34px; height: 34px; border-radius: 50%;
    background: var(--white);
  }
  .back-brand .brand-name {
    color: var(--white); font-weight: 700;
    font-size: 24px; line-height: 1; white-space: nowrap;
  }
</style>
</head>
<body>
<main class="stage">
  <section class="card-front" aria-label="Business card front">
    <div class="front-brand">
      <span class="brand-dot"></span>
      <span class="brand-name">Northgate Law Collective</span>
    </div>
    <div class="holder">
      <p class="holder-name">Amy Stewart</p>
      <p class="holder-role">CEO</p>
    </div>
    <div class="divider"></div>
    <ul class="contact-list">
      <li><span class="label">p :</span> +1 555 010 2487</li>
      <li><span class="label">f :</span> +1 555 010 3391</li>
      <li><span class="label">e :</span> amy_stewart@northgatelaw.example</li>
      <li><span class="label label-wide">PO</span>: PO Box 214</li>
    </ul>
    <div class="web-band">northgatelaw.example</div>
  </section>

  <section class="card-back" aria-label="Business card back">
    <div class="back-brand">
      <span class="brand-dot"></span>
      <span class="brand-name">Northgate Law Collective</span>
    </div>
  </section>
</main>
</body>
</html>
```